Biz Card & Stationary: Modern, boutique appeal for vacation rental company for high end luxury homes
Biz Card + Folder + Letterhead + Envelope
Simple
Marla Whitcombe
Owner
2817 Maple Hollow Ln Austin TX 78529
marla@quolbi.com
www.quolbi.com
-may create image or graphic to use with logo -Need letterhead & envelopes in word format

```html
<!DOCTYPE html>
<html lang="en">
<head>
<meta charset="utf-8">
<title>Quolbi Business Card</title>
<link href="https://fonts.googleapis.com/css2?family=Questrial&display=swap" rel="stylesheet">
<style>
  :root {
    --teal: #3bb8c4;
    --grey: #6d6e71;
    --paper: #ffffff;
    --backdrop: #e9eaec;
  }
  * { box-sizing: border-box; margin: 0; padding: 0; }
  html, body { width: 1200px; height: 754px; overflow: hidden; }
  body {
    background: var(--backdrop);
    font-family: "Questrial", sans-serif;
    display: flex;
    align-items: center;
    justify-content: center;
    gap: 40px;
  }
  .card {
    position: relative;
    width: 540px;
    height: 310px;
    background: var(--paper);
    box-shadow: 0 6px 18px rgba(0,0,0,0.12);
    overflow: hidden;
  }
  .brand {
    display: flex;
    align-items: center;
    gap: 12px;
    color: var(--grey);
    font-weight: 400;
    text-transform: uppercase;
    letter-spacing: 6px;
    white-space: nowrap;
  }
  .brand-mark {
    width: 12px; height: 12px;
    background: var(--grey);
    flex: none;
  }
  .card-front .brand {
    position: absolute;
    left: 50%; top: 50%;
    transform: translate(-50%, -50%);
    font-size: 30px;
  }
  .card-back .brand {
    position: absolute;
    left: 36px; top: 110px;
    font-size: 26px;
  }
  .contact {
    position: absolute;
    left: 300px; top: 38px;
  }
  .contact-name {
    color: var(--teal);
    font-size: 15px;
    letter-spacing: 1.5px;
    text-transform: uppercase;
  }
  .contact-title {
    color: var(--grey);
    font-size: 10px;
    margin-top: 3px;
    margin-bottom: 14px;
  }
  .contact-list { list-style: none; }
  .contact-list li {
    display: flex;
    align-items: center;
    gap: 9px;
    color: var(--grey);
    font-size: 10.5px;
    height: 18px;
  }
  .contact-list svg { width: 12px; height: 12px; flex: none; }
  .wave { position: absolute; left: 0; bottom: 0; width: 540px; height: 150px; }
  .address {
    position: absolute;
    right: 30px; bottom: 18px;
    color: var(--paper);
    font-size: 11px;
    letter-spacing: 0.5px;
  }
</style>
</head>
<body>
  <section class="card card-front">
    <div class="brand"><span class="brand-mark"></span>Quolbi</div>
  </section>

  <section class="card card-back">
    <div class="brand"><span class="brand-mark"></span>Quolbi</div>

    <div class="contact">
      <p class="contact-name">Marla Whitcombe</p>
      <p class="contact-title">Owner</p>
      <ul class="contact-list">
        <li><svg viewBox="0 0 12 12"><circle cx="6" cy="6" r="6" fill="var(--teal)"/><path d="M4 3.2l1 1.3-.6.8a4 4 0 0 0 2.3 2.3l.8-.6 1.3 1-.6 1A5 5 0 0 1 3 4z" fill="#fff"/></svg>512 555 0148</li>
        <li><svg viewBox="0 0 12 12"><circle cx="6" cy="6" r="6" fill="var(--teal)"/><rect x="4" y="2.8" width="4" height="6.4" rx="0.8" fill="#fff"/></svg>512 555 0172</li>
        <li><svg viewBox="0 0 12 12"><circle cx="6" cy="6" r="6" fill="var(--teal)"/><rect x="3" y="4.5" width="6" height="4" fill="#fff"/><rect x="4" y="3" width="4" height="1.5" fill="#fff"/></svg>512 555 0190</li>
        <li><svg viewBox="0 0 12 12"><circle cx="6" cy="6" r="6" fill="var(--teal)"/><rect x="3" y="4" width="6" height="4.2" fill="#fff"/><path d="M3 4l3 2.3L9 4" stroke="var(--teal)" stroke-width="0.7" fill="none"/></svg>marla@quolbi.com</li>
        <li><svg viewBox="0 0 12 12"><circle cx="6" cy="6" r="6" fill="var(--teal)"/><circle cx="6" cy="6" r="3" stroke="#fff" stroke-width="0.8" fill="none"/><path d="M3 6h6M6 3v6" stroke="#fff" stroke-width="0.7"/></svg>www.quolbi.com</li>
      </ul>
    </div>

    <svg class="wave" viewBox="0 0 540 150" preserveAspectRatio="none">
      <path d="M0 86 C150 40 330 70 540 10 L540 22 C330 84 150 58 0 102 Z" fill="var(--grey)"/>
      <path d="M0 104 C160 62 330 92 540 34 L540 150 L0 150 Z" fill="var(--teal)"/>
    </svg>
    <p class="address">2817 Maple Hollow Ln, Austin TX 78529</p>
  </section>
</body>
</html>
```